Verdant Loop Advisors, LLC

I am looking for a simple, clear layout with my logo prominent and embossed, on the best quality card stock available. I would like the business name and phone number included on the card as well......I dont want my name anywhere on the card and I would like my logo embossed on the card......something simple with a white back......open to designs as long as they go along with recycling symbols and green type stuff.....The address, website, cell number, fax number, and email are listed below

5374 Tillbury Fenwood Road
Larkfield, MD 20799

c. 240.555.0143 f. 240.555.0187
e. sales@verdantloopadvisors.example
w. www.verdantloopadvisors.example

Industry/Entity Type

Recycling

```html
<!DOCTYPE html>
<html lang="en">
<head>
<meta charset="utf-8">
<title>Verdant Loop Advisors, LLC — Business Card</title>
<link href="https://fonts.googleapis.com/css2?family=Michroma&display=swap" rel="stylesheet">
<style>
  :root {
    --backdrop: #e6e4df;
    --card: #f5f5f0;
    --ink: #141414;
    --green: #1f6b36;
    --green-faint: #d3e0d3;
  }
  html, body {
    margin: 0;
    width: 1200px;
    height: 1000px;
    overflow: hidden;
    background: var(--backdrop);
  }
  .stage {
    position: relative;
    width: 1200px;
    height: 1000px;
  }
  .business-card {
    position: absolute;
    left: 180px;
    top: 260px;
    width: 840px;
    height: 480px;
    background: var(--card);
    box-shadow: 0 10px 30px rgba(0,0,0,0.18);
    overflow: hidden;
    font-family: "Michroma", sans-serif;
    color: var(--ink);
  }
  .brand-accent {
    position: absolute;
    right: -150px;
    top: 70px;
    width: 380px;
    height: 380px;
    border-radius: 50%;
    background: var(--green-faint);
  }
  .brand {
    position: absolute;
    left: 60px;
    top: 74px;
    display: flex;
    align-items: center;
    gap: 20px;
  }
  .brand-mark {
    width: 64px;
    height: 64px;
    background: var(--green);
    flex: none;
  }
  .brand-name {
    margin: 0;
    font-size: 31px;
    font-weight: 400;
    line-height: 1.25;
    letter-spacing: 1px;
    color: var(--ink);
    text-transform: uppercase;
  }
  .address {
    position: absolute;
    left: 60px;
    top: 262px;
    margin: 0;
    font-style: normal;
    font-size: 21px;
    line-height: 1.45;
  }
  .contact-list {
    position: absolute;
    left: 60px;
    top: 352px;
    margin: 0;
    padding: 0;
    list-style: none;
    font-size: 19px;
    line-height: 1.5;
  }
  .contact-list li {
    display: flex;
    align-items: center;
    gap: 10px;
  }
  .contact-list .phone-row {
    font-size: 21px;
  }
  .contact-icon {
    width: 20px;
    height: 20px;
    fill: var(--green);
    flex: none;
  }
  .fax-gap { margin-left: 10px; }
</style>
</head>
<body>
<main class="stage">
  <section class="business-card" aria-label="Verdant Loop Advisors business card">
    <div class="brand-accent" aria-hidden="true"></div>

    <div class="brand">
      <div class="brand-mark" aria-hidden="true"></div>
      <h1 class="brand-name">Verdant Loop<br>Advisors, LLC</h1>
    </div>

    <address class="address">
      5374 Tillbury Fenwood Road<br>
      Larkfield, MD 20799
    </address>

    <ul class="contact-list">
      <li class="phone-row">
        <svg class="contact-icon" viewBox="0 0 20 20" aria-label="Cell"><rect x="5" y="1" width="10" height="18" rx="2"/><rect x="7" y="4" width="6" height="10" fill="#f5f5f0"/></svg>
        <span>240.555.0143</span>
        <svg class="contact-icon fax-gap" viewBox="0 0 20 20" aria-label="Fax"><rect x="5" y="2" width="10" height="6"/><rect x="1" y="7" width="18" height="9" rx="2"/><rect x="5" y="13" width="10" height="5"/></svg>
        <span>240.555.0187</span>
      </li>
      <li>
        <svg class="contact-icon" viewBox="0 0 20 20" aria-label="Email"><rect x="1" y="4" width="18" height="12" rx="1"/><path d="M1 5 L10 11 L19 5" stroke="#f5f5f0" stroke-width="1.6" fill="none"/></svg>
        <span>sales@verdantloopadvisors.example</span>
      </li>
      <li>
        <svg class="contact-icon" viewBox="0 0 20 20" aria-label="Website"><circle cx="10" cy="10" r="9"/><g stroke="#f5f5f0" stroke-width="1.2" fill="none"><ellipse cx="10" cy="10" rx="4" ry="9"/><path d="M1 10 H19 M3 5.5 H17 M3 14.5 H17"/></g></svg>
        <span>www.verdantloopadvisors.example</span>
      </li>
    </ul>
  </section>
</main>
</body>
</html>
```